Mental health agency needs an ad for brochure

Please provide us with a half page (W 8.5 inches x H 5.5 inches) advertising our company. We are a mental health agency that provides training, education, and consultation for companies that serve children, adolescents, or adults. We can offer training and education to help companies better serve their clientele and consultation about how companies are currently working with their staff or clientele. Our website is www.quellbrook.com and they can contact us at info@haverstoneinstitute.com or 503-847-2163.

```html
<!DOCTYPE html>
<html lang="en">
<head>
<meta charset="utf-8">
<title>Haverstone Institute Northwest – Half Page Ad</title>
<link rel="stylesheet" href="https://fonts.googleapis.com/css2?family=Exo+2:ital,wght@0,400;0,700;1,400&family=Merriweather:wght@700;900&display=swap">
<style>
  :root{
    --navy:#0b2d6b;
    --navy-deep:#082a66;
    --cyan:#0aa3cc;
    --cyan-soft:#1a9fc8;
    --ink:#1b1b1b;
    --paper:#f4f5f7;
    --stage:#d9d9d9;
    --royal:#2a4f9a;
  }
  *{margin:0;padding:0;box-sizing:border-box}
  html,body{width:1200px;height:900px;overflow:hidden;background:var(--stage)}
  .ad{
    position:absolute;left:40px;top:87.5px;width:1760px;height:1138px;
    transform:scale(0.63636);transform-origin:0 0;
    background:var(--paper);overflow:hidden;
  }
  .ad__shapes{position:absolute;inset:0;width:1760px;height:1138px}
  .brand{position:absolute;left:80px;top:58px;width:480px;text-align:center}
  .brand__mark{width:170px;height:170px;border-radius:50%;background:var(--navy);margin:0 auto 40px}
  .brand__name{font-family:"Exo 2",sans-serif;font-weight:700;font-size:34px;line-height:40px;color:var(--navy)}
  .intro{position:absolute;left:103px;top:432px;font-family:"Merriweather",serif}
  .intro__lead{color:#fff;font-weight:900;font-size:43px;line-height:52px}
  .intro__body{color:var(--cyan);font-weight:700;font-size:29px;line-height:42px;margin-top:6px}
  .provide__title{position:absolute;left:580px;width:600px;top:722px;text-align:center;font-family:"Merriweather",serif;font-weight:900;font-size:38px;color:var(--navy)}
  .col{position:absolute;top:782px;text-align:center;font-family:"Exo 2",sans-serif;font-size:22.5px;line-height:29.6px;color:var(--ink)}
  .col--left{left:118px;width:430px}
  .col--mid{left:645px;width:470px}
  .col--right{left:1190px;width:460px}
  .col em{font-style:italic}
  .col .hl{color:var(--cyan);font-weight:700}
  .col__list{margin-top:6px}
  .divider{position:absolute;top:803px;width:2px;height:178px;background:var(--navy)}
  .divider--a{left:598px}
  .divider--b{left:1150px}
  .cta{position:absolute;left:0;top:982px;width:1760px;text-align:center;font-family:"Exo 2",sans-serif;font-weight:700;font-size:42px;color:var(--navy)}
  .cta span{background:var(--paper);padding:0 14px;position:relative}
  .cta::before{content:"";position:absolute;left:0;right:0;top:26px;height:2px;background:var(--navy)}
  .contact{position:absolute;top:1042px;height:96px;display:flex;align-items:center;gap:20px;font-family:"Exo 2",sans-serif;font-weight:700;font-size:39px;color:#fff}
  .contact--web{left:102px}
  .contact--mail{left:650px}
  .contact--phone{left:1340px}
  .contact svg{flex:none}
</style>
</head>
<body>
<div class="ad">
  <svg class="ad__shapes" viewBox="0 0 1760 1138">
    <defs>
      <linearGradient id="familyOutdoor" x1="0" y1="0" x2="0" y2="1">
        <stop offset="0" stop-color="#c9cdd0"/>
        <stop offset="0.3" stop-color="#6f7c55"/>
        <stop offset="0.65" stop-color="#b59a7c"/>
        <stop offset="1" stop-color="#5d6a82"/>
      </linearGradient>
      <linearGradient id="familyIndoor" x1="0" y1="0" x2="1" y2="1">
        <stop offset="0" stop-color="#b8bcc0"/>
        <stop offset="0.5" stop-color="#7a6a66"/>
        <stop offset="1" stop-color="#c9a94a"/>
      </linearGradient>
      <clipPath id="bigClip"><circle cx="1300" cy="355" r="362"/></clipPath>
    </defs>
    <path d="M800 0 L1000 0 A390 390 0 0 0 870 260 L752 260 A500 500 0 0 1 800 0Z" fill="var(--navy)"/>
    <path d="M1700 160 L1760 190 L1760 340 L1710 330 Z" fill="var(--cyan)"/>
    <circle cx="1300" cy="355" r="378" fill="none" stroke="var(--navy)" stroke-width="3"/>
    <rect x="900" y="0" width="860" height="720" fill="url(#familyOutdoor)" clip-path="url(#bigClip)" role="img" aria-label="Photo of a laughing family with two children and a dog sitting outdoors by a lake"/>
    <path d="M0 427 C200 350 470 360 700 450 L760 620 C600 720 420 770 0 705 Z" fill="var(--navy-deep)"/>
    <path d="M230 762 C480 770 650 700 760 610 L780 640 C640 730 470 775 230 762 Z" fill="var(--cyan)"/>
    <circle cx="890" cy="430" r="258" fill="var(--paper)" stroke="var(--cyan-soft)" stroke-width="3"/>
    <circle cx="890" cy="430" r="246" fill="url(#familyIndoor)" role="img" aria-label="Photo of a smiling father hugged by his daughter and partner at home"/>
    <circle cx="875" cy="165" r="51" fill="var(--cyan-soft)"/>
    <circle cx="1582" cy="617" r="60" fill="var(--royal)"/>
    <rect x="0" y="1042" width="1760" height="96" fill="var(--navy)"/>
    <polygon points="583,1042 1280,1042 1320,1138 623,1138" fill="var(--cyan)"/>
  </svg>

  <div class="brand">
    <div class="brand__mark"></div>
    <p class="brand__name">Haverstone Institute<br>Northwest, LLC</p>
  </div>

  <div class="intro">
    <p class="intro__lead">We are a<br>Mental Health Agency</p>
    <p class="intro__body">that provides training, education,<br>and consultation for companies<br>that serve children,<br>adolescents, or adults.</p>
  </div>

  <h2 class="provide__title">WHAT WE PROVIDE</h2>

  <p class="col col--left">Reduce stress and develop poise in<br>managing behaviors in your <span class="hl">school or<br>non-profit organization</span> with training in the<br>area of trauma, conflict resolution,<br>behavior management, and more.</p>
  <div class="divider divider--a"></div>
  <div class="col col--mid">
    <p>Additional training that can improve<br>client outcomes and staff satisfaction.</p>
    <p class="col__list"><em>Improved focus and attention<br>Decreased distractibility<br>Faster/better processing of information<br>Fewer child behavioral "meltdowns"/fights"</em></p>
  </div>
  <div class="divider divider--b"></div>
  <p class="col col--right">The opportunity to decrease staff stress,<br>burnout, absenteeism and increase staff<br>authenticity and openness using feedback<br>and heatmapping tools across teams and<br>departments in your <span class="hl">organization.</span></p>

  <div class="cta"><span>Get a Quote Today</span></div>

  <div class="contact contact--web">
    <svg width="36" height="36" viewBox="0 0 36 36" fill="none" stroke="var(--cyan)" stroke-width="2.2"><circle cx="18" cy="18" r="16"/><ellipse cx="18" cy="18" rx="7" ry="16"/><path d="M2 18h32M5 10h26M5 26h26"/></svg>
    www.quellbrook.com
  </div>
  <div class="contact contact--mail">
    <svg width="40" height="28" viewBox="0 0 40 28" fill="none" stroke="var(--navy)" stroke-width="2.4"><rect x="1.5" y="1.5" width="37" height="25"/><path d="M1.5 1.5L20 16 38.5 1.5M1.5 26.5L15 12M38.5 26.5L25 12"/></svg>
    info@haverstoneinstitute.com
  </div>
  <div class="contact contact--phone">
    <svg width="38" height="38" viewBox="0 0 38 38" fill="none" stroke="var(--cyan)" stroke-width="2.2"><circle cx="19" cy="19" r="17"/><path d="M13 10l4 5-2 2c1 3 3 5 6 6l2-2 5 4-2 3c-7 0-15-8-15-15z"/></svg>
    503-847-2163
  </div>
</div>
</body>
</html>
```